Real Estate Superstar Business Card Design

We need a business card design for a new superstar real estate sales team based out of the Greater Toronto Area. A bit about us: The Agent in charge is Derek Okonta. We are a hard working team that heavily depends on our defined knowledge, aggressive skills and strong attitude to continue delivering exceptional service with amazing results for buyers and sellers.

Information that should be included on the card:
NestCrest Summit Realty Inc. ,Brokerage
4312 Vandorf Cres. #17
Mississauga, ON L4T 2K6
Independently Owned & Operated

Dir: 647-318-4062
Off: 905-461-7373
Fax: 905-461-7370

Industry/Entity Type

Real Estate

Font styles to use
Script

Requirements
Must have
• -NestCrest Summit Logo
-Derek Okonta Logo

```html
<!DOCTYPE html>
<html lang="en">
<head>
<meta charset="utf-8">
<title>Derek Okonta – Business Card</title>
<link rel="stylesheet" href="https://fonts.googleapis.com/css2?family=Arimo&family=Didact+Gothic&family=Tinos:wght@700&display=swap">
<style>
  :root {
    --backdrop: #b9b9b9;
    --card: #ffffff;
    --sky: #3d9dd6;
    --navy: #0b527c;
    --brand: #0d5a8a;
    --accent: #ff7f0e;
    --ink: #111111;
  }
  html, body {
    margin: 0;
    width: 1200px;
    height: 1076px;
    overflow: hidden;
    background: var(--backdrop);
  }
  .card {
    position: absolute;
    left: 256px;
    width: 652px;
    height: 351px;
    background: var(--card);
    border-radius: 9px;
    overflow: hidden;
  }
  .card--front { top: 115px; }
  .card--back { top: 535px; }
  .card__waves {
    position: absolute;
    inset: 0;
    width: 652px;
    height: 351px;
  }
  .brand-mark {
    position: absolute;
    display: flex;
    align-items: center;
    gap: 10px;
    font-family: "Didact Gothic", sans-serif;
    font-size: 27px;
    letter-spacing: 1px;
    color: var(--brand);
    white-space: nowrap;
  }
  .brand-mark__square {
    width: 22px;
    height: 22px;
    background: var(--accent);
  }
  .card--front .brand-mark { left: 30px; top: 70px; }
  .card--back .brand-mark { left: 0; right: 0; top: 90px; justify-content: center; }
  .agent {
    position: absolute;
    left: 29px;
    top: 186px;
  }
  .agent__name {
    margin: 0;
    font-family: "Tinos", serif;
    font-weight: 700;
    font-size: 52px;
    line-height: 1;
    color: var(--ink);
  }
  .agent__title {
    margin: 2px 0 0 1px;
    font-family: "Arimo", sans-serif;
    font-size: 20px;
    color: var(--ink);
  }
  .brokerage {
    position: absolute;
    left: 390px;
    top: 22px;
    width: 250px;
  }
  .brokerage__mark {
    display: flex;
    align-items: center;
    gap: 7px;
    font-family: "Didact Gothic", sans-serif;
    font-size: 16px;
    letter-spacing: 0.5px;
    color: var(--brand);
    white-space: nowrap;
    margin-bottom: 4px;
  }
  .brokerage__square {
    width: 12px;
    height: 12px;
    background: var(--accent);
  }
  .contact {
    margin: 0;
    font-family: "Didact Gothic", sans-serif;
    font-size: 13px;
    line-height: 17px;
    color: var(--ink);
    font-style: normal;
    white-space: nowrap;
  }
  .contact__note {
    font-size: 11.5px;
    color: var(--brand);
  }
  .website {
    position: absolute;
    font-family: "Didact Gothic", sans-serif;
    font-weight: 700;
    font-size: 15px;
    color: #ffffff;
    letter-spacing: 0.3px;
    -webkit-text-stroke: 0.4px #ffffff;
  }
  .card--front .website { right: 22px; top: 311px; }
  .card--back .website { left: 0; right: 0; text-align: center; top: 311px; }
</style>
</head>
<body>

<section class="card card--front">
  <svg class="card__waves" viewBox="0 0 652 351" aria-hidden="true">
    <path d="M0,301 Q400,290 652,162 L652,351 L0,351 Z" fill="var(--sky)"/>
    <path d="M0,315 Q360,305 652,267 L652,351 L0,351 Z" fill="var(--navy)"/>
  </svg>
  <div class="brand-mark"><span class="brand-mark__square"></span>DEREK OKONTA</div>
  <div class="brokerage">
    <div class="brokerage__mark"><span class="brokerage__square"></span>NESTCREST SUMMIT</div>
    <address class="contact">
      Realty Inc., Brokerage<br>
      4312 Vandorf Cres. #17<br>
      Mississauga, ON L4T 2K6<br>
      Dir: 647-318-4062<br>
      Off: 905-461-7373 &nbsp;Fax: 905-461-7370<br>
      <span class="contact__note">Independently Owned &amp; Operated</span>
    </address>
  </div>
  <div class="agent">
    <h1 class="agent__name">Derek Okonta</h1>
    <p class="agent__title">Marketing Agent</p>
  </div>
  <div class="website">www.okontahomes.com</div>
</section>

<section class="card card--back">
  <svg class="card__waves" viewBox="0 0 652 351" aria-hidden="true">
    <rect x="0" y="155" width="652" height="196" fill="var(--sky)"/>
    <path d="M0,0 H652 V163 Q330,255 0,178 Z" fill="var(--card)"/>
    <rect x="0" y="220" width="652" height="131" fill="var(--navy)"/>
  </svg>
  <div class="brand-mark"><span class="brand-mark__square"></span>DEREK OKONTA</div>
  <div class="website">www.okontahomes.com</div>
</section>

</body>
</html>
```